Business card design for Velvet Harbor

We need business cards designed for our new marketing consulting company, Velvet Harbor. Our services include marketing strategy, go-to-market and launch planning, growth strategy, and execution. We serve medical technology and health technology companies, from startups to well-established growth companies.

The business cards should feel professional, credible, reliable and trustworthy, and should instill confidence. Also bold, creative, and modern.

The design must use the Velvet Harbor logo.

The primary brand color is this orange: #FF5501
A secondary color that you can use is this gray: #282B2D
I would prefer only to use the orange and gray. But if you feel you really need an additional accent color (please use it very sparingly, as little as possible), you can use this blue for small accent purposes: #009FED

Attached are the logo files. The main logo is the one with a little bit of orange on the left and the rest is gray.

The business card should include the following:

Velvet Harbor logo
First name and last name
Title
Email address
Phone number and type (in whatever order looks best for the design
Website (the website does not need to be in the same block as the personal info)

For example:

Nessa Pryle
Founder & Principal
nessa@velvetharbor.com
+1.628.309.4156 mobile (can use "." or spaces in between blocks of numbers)
velvetharbor.com (somewhere on the card, it does not need to be with the personal info; and note that there is no "www." at the beginning)

Note that there will be no address listed on the business card.

Target Market(s)

Executives (CEO, head of marketing, head of sales) at medical technology and health technology companies, mostly in their 40s and older, well-educated, often with advanced degrees. They are strategic thinkers, responsible for budgets, and familiar with P&L. Their comfort with and trust in using outside consultants varies.

Industry/Entity Type

Medical technology and health technology companies.

Contact Information for Business Card

See project description

Font styles to use
Sans Serif

Requirements
Must have
• Logo and see Business card details section above.

```html
<!DOCTYPE html>
<html lang="en">
<head>
<meta charset="utf-8">
<title>Velvet Harbor — Business Card</title>
<link rel="stylesheet" href="https://fonts.googleapis.com/css2?family=Michroma&family=Poppins:wght@400;500&display=swap">
<style>
  :root {
    --orange: #FF5501;
    --graphite: #282B2D;
    --card: #0d0d0e;
    --card-edge: #161718;
    --stage: #1f2021;
    --white: #f4f4f4;
    --muted: #5a5d60;
  }
  * { margin: 0; padding: 0; box-sizing: border-box; }
  html, body {
    width: 1200px;
    height: 900px;
    overflow: hidden;
    background: var(--stage);
  }
  .stage {
    width: 1200px;
    height: 900px;
    display: flex;
    flex-direction: column;
    align-items: center;
    justify-content: center;
    gap: 40px;
  }
  .card {
    position: relative;
    width: 680px;
    height: 389px;
    border-radius: 22px;
    background: radial-gradient(ellipse at 70% 20%, var(--card-edge) 0%, var(--card) 70%);
    box-shadow: 0 12px 30px rgba(0,0,0,0.5);
    overflow: hidden;
  }
  .accent-rule {
    position: absolute;
    left: 42px;
    right: 48px;
    bottom: 40px;
    height: 12px;
    display: flex;
    align-items: center;
    gap: 12px;
  }
  .accent-rule .dot {
    width: 11px; height: 11px;
    border-radius: 50%;
    background: var(--orange);
    flex: none;
  }
  .accent-rule .line {
    flex: 1;
    height: 5px;
    border-radius: 3px;
    background: var(--orange);
  }
  .brand {
    display: flex;
    align-items: center;
    gap: 12px;
  }
  .brand .marker {
    width: 12px; height: 12px;
    background: var(--orange);
    flex: none;
  }
  .brand .brand-name {
    font-family: "Poppins", sans-serif;
    font-weight: 500;
    color: var(--white);
    font-size: 26px;
    line-height: 1;
    white-space: nowrap;
  }
  /* Front */
  .card-front .brand {
    position: absolute;
    left: 58px;
    top: 178px;
  }
  .card-front .divider {
    position: absolute;
    left: 318px;
    top: 92px;
    width: 1px;
    height: 200px;
    background: linear-gradient(to bottom, transparent, var(--muted), transparent);
  }
  .contact {
    position: absolute;
    left: 352px;
    top: 104px;
  }
  .contact .person-name {
    font-family: "Michroma", sans-serif;
    font-size: 22px;
    color: var(--white);
    letter-spacing: 0.12em;
    text-transform: uppercase;
    white-space: nowrap;
  }
  .contact .person-title {
    font-family: "Poppins", sans-serif;
    font-size: 19px;
    color: var(--orange);
    margin-top: 2px;
  }
  .contact .details {
    list-style: none;
    margin-top: 24px;
    display: flex;
    flex-direction: column;
    gap: 8px;
  }
  .contact .details li {
    display: flex;
    align-items: center;
    gap: 10px;
    font-family: "Poppins", sans-serif;
    font-size: 17px;
    color: var(--white);
    white-space: nowrap;
  }
  .contact .icon { width: 26px; height: 26px; flex: none; }
  /* Back */
  .card-back .back-content {
    position: absolute;
    inset: 0 0 60px 0;
    display: flex;
    flex-direction: column;
    align-items: center;
    justify-content: center;
    gap: 22px;
  }
  .card-back .brand .marker { width: 16px; height: 16px; }
  .card-back .brand .brand-name { font-size: 36px; }
  .card-back .website {
    font-family: "Poppins", sans-serif;
    font-size: 18px;
    color: var(--white);
    letter-spacing: 0.02em;
  }
</style>
</head>
<body>
<main class="stage">
  <section class="card card-front" aria-label="Business card front">
    <div class="brand">
      <span class="marker" aria-hidden="true"></span>
      <span class="brand-name">Velvet Harbor</span>
    </div>
    <div class="divider" aria-hidden="true"></div>
    <div class="contact">
      <p class="person-name">Nessa Pryle</p>
      <p class="person-title">Founder &amp; Principal</p>
      <ul class="details">
        <li>
          <svg class="icon" viewBox="0 0 26 26" aria-hidden="true">
            <circle cx="13" cy="13" r="11.5" fill="none" stroke="#FF5501" stroke-width="1.6"/>
            <rect x="9" y="6.5" width="8" height="13" rx="1.5" fill="none" stroke="#FF5501" stroke-width="1.5"/>
            <line x1="12" y1="17.2" x2="14" y2="17.2" stroke="#FF5501" stroke-width="1.4"/>
          </svg>
          <span>+1.628.309.4156</span>
        </li>
        <li>
          <svg class="icon" viewBox="0 0 26 26" aria-hidden="true">
            <circle cx="13" cy="13" r="11.5" fill="none" stroke="#FF5501" stroke-width="1.6"/>
            <rect x="6.5" y="8.5" width="13" height="9" rx="1" fill="#FF5501"/>
            <polyline points="6.8,9 13,14 19.2,9" fill="none" stroke="#0d0d0e" stroke-width="1.3"/>
          </svg>
          <span>nessa@velvetharbor.com</span>
        </li>
      </ul>
    </div>
    <div class="accent-rule" aria-hidden="true"><span class="dot"></span><span class="line"></span></div>
  </section>

  <section class="card card-back" aria-label="Business card back">
    <div class="back-content">
      <div class="brand">
        <span class="marker" aria-hidden="true"></span>
        <span class="brand-name">Velvet Harbor</span>
      </div>
      <p class="website">velvetharbor.com</p>
    </div>
    <div class="accent-rule" aria-hidden="true"><span class="dot"></span><span class="line"></span></div>
  </section>
</main>
</body>
</html>
```